Book cover needed for self help business book

Book cover needed and I will provide back cover blurb and barcode to the winning designer. Book may be too small for spine, but I will give you the page number details to confirm. Book information below:

Title: Nine Winters a Trader
Subtitle: Proven Market Methods That Keep Paying Off Now
Author: Maribel Okonte

Design should be clean, modern, and bold—something that appeals to everyday entrepreneurs and resellers. The cover should reflect grit, real-world hustle, and long-term wisdom without looking overly corporate or flashy. I am open to your creative ideas.

I am open to modern designs, but also designs of rugged old covers that simulate a book that may have aged over the years.

I prefer not to have pictures or silhouettes of people

Requirements
Nice to have
• I am open to modern designs, but also designs of rugged old covers that simulate a book that may have aged over the years.
Should not have
• Pictures or silhouettes of people

```html
<!DOCTYPE html>
<html lang="en">
<head>
<meta charset="utf-8">
<title>Nine Winters a Trader — Book Cover</title>
<link href="https://fonts.googleapis.com/css2?family=Montserrat:wght@500;600;700;800&display=swap" rel="stylesheet">
<style>
  :root {
    --page: #ffffff;
    --navy: #0b1630;
    --gold-dark: #b5801f;
    --gold-mid: #e0aa3a;
    --gold-light: #f3cf6b;
    --white: #ffffff;
    --teal: #3fb6c4;
    --sky: #a8e4ea;
    --orange: #e48a3c;
    --violet: #6b3c6e;
  }
  * { margin: 0; padding: 0; box-sizing: border-box; }
  html, body {
    width: 1200px; height: 1200px; overflow: hidden;
    background: var(--page);
  }
  .cover {
    position: absolute;
    left: 219px; top: 28px;
    width: 762px; height: 1143px;
    background: var(--navy);
    overflow: hidden;
    font-family: 'Montserrat', sans-serif;
  }
  .title {
    position: absolute; left: 0; right: 0; top: 58px;
    text-align: center;
    font-weight: 700;
    line-height: 1;
    background: linear-gradient(90deg, var(--gold-dark) 0%, var(--gold-mid) 30%, var(--gold-light) 55%, var(--gold-mid) 75%, var(--gold-dark) 100%);
    -webkit-background-clip: text; background-clip: text;
    color: transparent;
  }
  .title-line-top { display: block; font-size: 70px; letter-spacing: 0px; }
  .title-line-main { display: block; font-size: 146px; letter-spacing: -2px; margin-top: 10px; }
  .subtitle {
    position: absolute; left: 0; right: 0; top: 318px;
    text-align: center;
    color: var(--white);
    font-weight: 500;
    font-size: 29px;
    line-height: 40px;
    letter-spacing: 1px;
    text-transform: uppercase;
  }
  .illustration {
    position: absolute;
    left: 34px; top: 405px;
    width: 694px; height: 650px;
    background:
      radial-gradient(ellipse 32% 38% at 50% 48%, var(--sky) 0%, rgba(63,182,196,0.9) 45%, rgba(63,182,196,0) 100%),
      radial-gradient(ellipse 30% 45% at 18% 45%, rgba(228,138,60,0.95) 0%, rgba(228,138,60,0) 100%),
      radial-gradient(ellipse 28% 45% at 84% 50%, rgba(228,138,60,0.9) 0%, rgba(228,138,60,0) 100%),
      radial-gradient(ellipse 45% 30% at 50% 88%, rgba(107,60,110,0.9) 0%, rgba(107,60,110,0) 100%),
      radial-gradient(ellipse 50% 50% at 50% 50%, rgba(63,182,196,0.6) 0%, rgba(11,22,48,0) 100%);
    -webkit-mask-image: radial-gradient(ellipse 52% 52% at 50% 50%, #000 60%, transparent 100%);
    mask-image: radial-gradient(ellipse 52% 52% at 50% 50%, #000 60%, transparent 100%);
  }
  .author {
    position: absolute; left: 0; right: 0; bottom: 12px; top: auto;
    top: 1068px;
    text-align: center;
    color: var(--white);
    font-weight: 500;
    font-size: 62px;
    line-height: 1;
    letter-spacing: 3px;
    text-transform: uppercase;
  }
</style>
</head>
<body>
  <main class="cover">
    <h1 class="title">
      <span class="title-line-top">NINE WINTERS A</span>
      <span class="title-line-main">TRADER</span>
    </h1>
    <p class="subtitle">Proven Market Methods That<br>Keep Paying Off Now</p>
    <div class="illustration" role="img" aria-label="Whimsical painted scene of a floating robot among colourful alien rock formations, spiky pods and drifting orbs in teal, orange and violet"></div>
    <p class="author">Maribel Okonte</p>
  </main>
</body>
</html>
```